Plumweave Inc. Website & Korvix Apps Landing Pages

We need a web site design for our company. We develop software and do various consultant projects for our clients. Our products focus on the mobile platform, mainly the Korvix (business, games, social, etc.). We want to communicate that our software is simple and good as candy. The web pages should be fun to look at not loosing seriousness and credibility. Web 2.0 style and 960 grid system a must. We are opened to any overall site colour scheme suggestions (look at the sites we like below).

Must haves:
- Our logo should be seen on the site and look great on it :-) (preview attached below)
- Main home page and app landing page.
- Section links/tabs on the home page (home,apps,support,blog,contact,about)
- No text in images
- Style sheet

Looks we like:
- http://x7k3lmq9pwrtzv.pixelmoorvault.net/412_Zelto_Site/final_large.jpg
- http://x7k3lmq9pwrtzv.pixelmoorvault.net/Premium_71_Illustrative_Korvix_Landing_Page/final.jpg
- http://grelmwick.com/
- http://dorniply.ca/
- http://quatzel.com/

Industry/Entity Type

Business

Requirements
Must have
• - Company logo should look great on pages.
• - Main home page and app landing page.
• - Section links/tabs on the home page (home,apps,support,blog,contact,about)
• - Web 2.0 style.
• - 960 grid system (12 col, 16 col).
• - Sliced ann optmized
• - Exported in all major formats (psd,ai,eps,png,jpeg,etc)
• - Style sheet
Should not have
• - Text in images

```html
<!DOCTYPE html>
<html lang="en">
<head>
<meta charset="utf-8">
<title>Plumweave Inc. — Apps</title>
<link rel="stylesheet" href="https://fonts.googleapis.com/css2?family=Arimo:ital,wght@0,400;0,700;1,400&family=Libre+Baskerville:ital@1&display=swap">
<style>
:root{
  --ink:#1c1c1c;
  --red:#d0141e;
  --red-deep:#a80c14;
  --ribbon:#f2566a;
  --paper:#efefef;
  --card:#ffffff;
  --text:#333333;
  --panel:#a9a9a9;
  --white:#ffffff;
  --device-dark:#2a2a2a;
  --device-mid:#6a6a6a;
  --device-screen:#8e5a66;
}
*{box-sizing:border-box;margin:0;padding:0}
html,body{width:1200px;height:1000px;overflow:hidden}
body{font-family:"Arimo",Arial,sans-serif;color:var(--text);background:var(--paper);position:relative}

.topbar{position:absolute;left:0;top:0;width:1200px;height:45px;background:var(--ink)}
.main-nav{position:absolute;right:105px;top:0;height:45px;display:flex;gap:24px;align-items:center}
.main-nav a{color:var(--white);font-size:14px;font-weight:700;text-decoration:none}
.main-nav a.is-current{color:var(--red);font-weight:400}

.hero{position:absolute;left:0;top:45px;width:1200px;height:399px;
  background:linear-gradient(90deg,#fbe9ea 0%,#f8c9cd 35%,#f07c86 62%,#c4121b 80%,#a80c14 100%);overflow:hidden}
.brand{position:absolute;left:93px;top:40px;display:flex;align-items:center;gap:14px}
.brand-dot{width:46px;height:46px;border-radius:50%;background:var(--red)}
.brand-name{font-size:58px;font-weight:700;color:var(--red);letter-spacing:-1px}
.hero-title{position:absolute;left:96px;top:127px;width:420px;font-size:20px;line-height:25px;color:var(--red);font-weight:400}
.hero-points{position:absolute;left:96px;top:189px;width:420px;list-style:none}
.hero-points li{font-size:13.5px;line-height:19px;color:var(--ink);padding-left:16px;position:relative}
.hero-points li::before{content:"";position:absolute;left:2px;top:8px;width:4px;height:4px;border-radius:50%;background:var(--ink)}

.platforms{position:absolute;left:93px;top:315px;width:366px;height:45px;border-radius:23px;background:var(--ink);display:flex;align-items:center;padding:0 18px}
.platforms-label{font-family:"Libre Baskerville",Georgia,serif;font-style:italic;color:var(--white);font-size:16px;flex:1}
.platforms-icons{display:flex;gap:12px}
.platforms-icons span{width:20px;height:20px;border-radius:50%;background:#9a9a9a}

.device-art{position:absolute;left:600px;top:88px;width:520px;height:500px;
  background:linear-gradient(180deg,rgba(40,40,40,.85) 0%,rgba(90,70,76,.85) 45%,rgba(30,30,30,.9) 100%);
  border-radius:30px}

.buy-now{position:absolute;left:578px;top:210px;width:255px;height:72px;background:var(--ribbon);display:flex;align-items:center;justify-content:center;gap:18px;
  box-shadow:0 3px 6px rgba(0,0,0,.25)}
.buy-now span{font-size:36px;font-weight:700;color:#3a1114}

.dropdown{position:absolute;left:915px;top:50px;width:203px;height:178px;background:var(--ink);border-radius:6px;padding:12px 16px;list-style:none;box-shadow:0 4px 10px rgba(0,0,0,.4)}
.dropdown li{font-size:13px;color:var(--white);line-height:30.5px;padding-left:18px;position:relative}
.dropdown li::before{content:"";position:absolute;left:2px;top:14px;width:4px;height:4px;border-radius:50%;background:var(--red)}
.dropdown li.is-current{color:var(--red)}

.content{position:absolute;left:288px;top:444px;width:525px;height:504px;background:var(--card);box-shadow:0 0 14px rgba(0,0,0,.12)}
.side-tabs{position:absolute;left:102px;top:486px;width:186px;list-style:none}
.side-tab{height:45px;display:flex;align-items:center;gap:16px;padding-left:4px;margin-bottom:4px;font-size:18px;color:var(--ink)}
.side-tab.is-active{background:linear-gradient(180deg,#3a3a3a,#1e1e1e);color:var(--white);border-radius:4px 0 0 4px}
.tab-icon{width:38px;height:38px;border-radius:4px;background:var(--red);display:flex;align-items:center;justify-content:center}

.article{position:absolute;left:333px;top:494px;width:460px}
.article h1{font-size:22px;font-weight:700;color:var(--ink);margin-bottom:10px}
.article p{font-size:12.5px;line-height:19.5px;color:var(--text)}
.pull-quote{position:relative;margin:22px 0 18px;padding-left:58px;padding-right:30px}
.pull-quote::before{content:"\201C";position:absolute;left:-4px;top:-22px;font-size:104px;font-family:Georgia,serif;font-weight:700;color:#555}
.pull-quote p{font-style:italic;color:var(--ink)}
.read-more{position:absolute;left:723px;top:897px;width:95px;height:29px;border-radius:5px;background:var(--ink);color:var(--white);font-size:11.5px;font-weight:700;display:flex;align-items:center;justify-content:center;gap:6px}

.slider-dots{position:absolute;left:937px;top:604px;display:flex;gap:5px}
.slider-dots span{width:12px;height:12px;border-radius:50%;background:#6d6d6d;box-shadow:inset 0 1px 2px rgba(0,0,0,.4)}
.slider-dots span.is-active{background:#dcdcdc}

.recent-posts{position:absolute;left:849px;top:645px;width:246px;height:243px;background:var(--panel);border-radius:6px;overflow:hidden}
.recent-posts h2{height:45px;background:linear-gradient(180deg,#333,#1d1d1d);color:var(--white);font-size:18px;font-weight:400;padding:13px 0 0 26px}
.recent-posts ul{list-style:none;padding:10px 16px 0 22px}
.recent-posts li{font-size:12.5px;line-height:18px;color:var(--ink);padding:5px 0 5px 18px;border-bottom:1px solid #bcbcbc;position:relative}
.recent-posts li:last-child{border-bottom:none}
.recent-posts li::before{content:"";position:absolute;left:2px;top:13px;width:7px;height:1px;background:#666}

.footer{position:absolute;left:0;top:948px;width:1200px;height:52px;background:var(--ink)}
.footer-brand{position:absolute;left:93px;top:12px;display:flex;align-items:center;gap:8px}
.footer-brand .brand-dot{width:22px;height:22px}
.footer-brand .brand-name{font-size:26px;letter-spacing:0}
.footer-nav{position:absolute;right:90px;top:0;height:52px;display:flex;gap:22px;align-items:center}
.footer-nav a{color:var(--white);font-size:13.5px;font-weight:700;text-decoration:none}
.footer-nav a.is-current{color:var(--red);font-weight:400}
</style>
</head>
<body>

<header class="topbar">
  <nav class="main-nav">
    <a class="is-current" href="#">Home</a>
    <a href="#">Products</a>
    <a href="#">Blog</a>
    <a href="#">Contact</a>
  </nav>
</header>

<section class="hero">
  <div class="brand"><span class="brand-dot"></span><span class="brand-name">Plumweave</span></div>
  <h2 class="hero-title">Vulputate velit esse lorem consequat vellorum illum dolore eu feugiat ipsum dolor sit amet</h2>
  <ul class="hero-points">
    <li>Human per seacula quarta decima et quinta dima eodebis consequat vel illum dolore eu feugiat nulla facilisis.</li>
    <li>Nunc putamus parum, claram antep osuerit litterarum formas lorem ipsum dolor sit amet consectetuer adipiscing elit quin.</li>
    <li>Littera gothica quam nunc putamus parum clantepo a com nunc</li>
  </ul>
  <div class="platforms">
    <span class="platforms-label">Supported Platforms</span>
    <span class="platforms-icons"><span></span><span></span><span></span><span></span></span>
  </div>
</section>

<div class="device-art" role="img" aria-label="Two Korvix phones, one seen from an angle behind one facing front showing an app screen"></div>

<div class="buy-now">
  <span>Buy Now</span>
  <svg width="30" height="26" viewBox="0 0 30 26" aria-hidden="true"><path d="M0 9h16V0l14 13-14 13v-9H0z" fill="#3a1114"/></svg>
</div>

<ul class="dropdown">
  <li>Ut sagittis ultrices urna</li>
  <li>Neque porro quisquam</li>
  <li class="is-current">Nam libero tempore</li>
  <li>Magna suspendisse</li>
  <li>Ut sagittis ultrices urna</li>
</ul>

<main>
  <div class="content"></div>

  <ul class="side-tabs">
    <li class="side-tab is-active"><span class="tab-icon"><svg width="24" height="16" viewBox="0 0 24 16" aria-hidden="true"><ellipse cx="12" cy="8" rx="11" ry="6.5" fill="none" stroke="#fff" stroke-width="2"/><circle cx="12" cy="8" r="3" fill="#fff"/></svg></span>Features</li>
    <li class="side-tab"><span class="tab-icon"><svg width="22" height="22" viewBox="0 0 22 22" aria-hidden="true"><path d="M5 2h12v6a6 6 0 0 1-12 0z M9 14h4v3h3v3H6v-3h3z" fill="#fff"/></svg></span>Reviews</li>
    <li class="side-tab"><span class="tab-icon"><svg width="24" height="22" viewBox="0 0 24 22" aria-hidden="true"><rect x="2" y="2" width="20" height="14" rx="1" fill="none" stroke="#fff" stroke-width="2"/><path d="M8 20h8M12 16v4" stroke="#fff" stroke-width="2"/></svg></span>Screenshots</li>
    <li class="side-tab"><span class="tab-icon"><svg width="24" height="24" viewBox="0 0 24 24" aria-hidden="true"><circle cx="9" cy="10" r="5" fill="none" stroke="#fff" stroke-width="3" stroke-dasharray="3 2"/><circle cx="17" cy="17" r="3.5" fill="none" stroke="#fff" stroke-width="2.5" stroke-dasharray="2 1.5"/></svg></span>Specifications</li>
  </ul>

  <article class="article">
    <h1>Features</h1>
    <p>Quam nunc putamus parum claram anteposuerit litterarum formas sed at humanitatis per seacula quarta decima et quinta? Ipsum dolor sit amet elit onsectetuer adipiscing elit sed diam nonummy nibh euismod tincidunt ut. Zzril delenit augue duis dolore te feugait nulla facilisi nam liber tempor. Cum soluta nobis eleifend option congue nihil imperdiet, doming id quod mazim.</p>
    <blockquote class="pull-quote"><p>Doming id quod mazim placerat facer possim assum typi non habent? Euismod tincidunt ut laoreet dolore magna, aliquam erat volutpat ut wisi. Nonummy nibh enim ad minim veniam quis nostrud exerci tation ullamcorper. Formas humanitatis per seacula quarta decima et quinta decima eodem.</p></blockquote>
    <p>Magna aliquam erat volutpat ut wisi enim ad minim veniam. Insitam est usus legentis in iis qui facit eorum claritatem Investigationes.Doming id quod sed mazim placerat facer possim assum typi non habent? Euismod tincidunt ut laoreet dolore magna, aliquam erat volutpat ut wisi. Nonummy nibh enim ad minim veniam quis nostrud exerci tation ullamcorper. Formas humanitatis per seacula quarta decima et quinta decima eodem.Doming id quod mazim</p>
  </article>
  <a class="read-more">Read More <svg width="11" height="10" viewBox="0 0 11 10" aria-hidden="true"><path d="M1 9V5h6V2l4 3.5L7 9V7H3v2z" fill="#fff"/></svg></a>

  <div class="slider-dots"><span></span><span class="is-active"></span><span></span><span></span></div>

  <aside class="recent-posts">
    <h2>Recent Posts</h2>
    <ul>
      <li>Ut sagittis ultrices urna eget erat</li>
      <li>Neque porro quisquam est qui</li>
      <li>Nam libero tempore, cum soluta nobis</li>
      <li>Magna suspendisse eleifen</li>
      <li>Etiam placerat ipsum porttitor</li>
    </ul>
  </aside>
</main>

<footer class="footer">
  <div class="footer-brand"><span class="brand-dot"></span><span class="brand-name">Plumweave</span></div>
  <nav class="footer-nav">
    <a class="is-current" href="#">Home</a>
    <a href="#">Products</a>
    <a href="#">Blog</a>
    <a href="#">Contact</a>
  </nav>
</footer>

</body>
</html>
```